Korvane Motors business cards

We need business cards for our company Korvane Motors, based in Brisbane but trading world wide. We buy and sell Korvane Motors, generators and marine equipment. The design needs to be kept clean, simple but eye catching.
Please keep with our current logo (included) and further information can be included on request

Business

0792cd
33a6d7
85cae6
3276b5
0455a3
cedeed
cee9f5
ffffff

```html
<!DOCTYPE html>
<html lang="en">
<head>
<meta charset="utf-8">
<title>Korvane Motors business cards</title>
<link rel="stylesheet" href="https://fonts.googleapis.com/css2?family=Mulish:wght@400;700&display=swap">
<style>
  :root {
    --blue-deep: #0455a3;
    --blue-main: #3276b5;
    --blue-bright: #0792cd;
    --blue-sky: #33a6d7;
    --blue-soft: #85cae6;
    --ice: #cee9f5;
    --mist: #cedeed;
    --white: #ffffff;
    --ink: #5a5d62;
    --ink-light: #6e7176;
    --backdrop: #b9bbbe;
  }
  * { margin: 0; padding: 0; box-sizing: border-box; }
  html, body {
    width: 1200px;
    height: 871px;
    overflow: hidden;
  }
  body {
    background: var(--backdrop);
    font-family: "Mulish", Arial, sans-serif;
    position: relative;
  }
  .card {
    position: absolute;
    width: 540px;
    height: 310px;
    overflow: hidden;
    box-shadow: 0 10px 24px rgba(0,0,0,0.28);
  }

  /* Back of card */
  .card-back {
    left: 70px;
    top: 120px;
    background: linear-gradient(135deg, var(--blue-main) 0%, #2a68a6 60%, var(--blue-deep) 100%);
    color: var(--white);
  }
  .card-back .brand {
    position: absolute;
    left: 80px;
    top: 110px;
    display: flex;
    align-items: center;
    gap: 18px;
  }
  .brand-square {
    width: 80px;
    height: 80px;
    border-radius: 10px;
    background: var(--white);
  }
  .card-back .brand-name {
    font-weight: 700;
    font-size: 30px;
    line-height: 1.05;
    letter-spacing: 0.3px;
  }
  .card-back .website {
    position: absolute;
    left: 80px;
    top: 222px;
    font-size: 16px;
    letter-spacing: 0.5px;
    color: var(--ice);
  }

  /* Front of card */
  .card-front {
    left: 590px;
    top: 440px;
    background: var(--white);
  }
  .card-front .bolt {
    position: absolute;
    inset: 0;
    width: 100%;
    height: 100%;
  }
  .contact {
    position: absolute;
    left: 34px;
    top: 34px;
    color: var(--ink);
  }
  .contact .person {
    font-weight: 700;
    font-size: 21px;
    color: var(--ink);
    margin-bottom: 24px;
  }
  .contact .address {
    font-size: 12.5px;
    line-height: 1.45;
    color: var(--ink-light);
    margin-bottom: 16px;
  }
  .contact .lines {
    list-style: none;
    font-size: 12.5px;
    line-height: 1.75;
    color: var(--ink-light);
  }
  .contact .lines li {
    display: flex;
    align-items: center;
    gap: 12px;
  }
  .contact .lines svg {
    width: 13px;
    height: 13px;
    flex: none;
    stroke: var(--blue-main);
    fill: none;
    stroke-width: 1.4;
  }
  .card-front .brand {
    position: absolute;
    right: 26px;
    bottom: 30px;
    display: flex;
    align-items: center;
    gap: 10px;
    color: var(--white);
  }
  .card-front .brand-square {
    width: 48px;
    height: 48px;
    border-radius: 6px;
  }
  .card-front .brand-name {
    font-weight: 700;
    font-size: 24px;
    line-height: 1;
  }
  .card-front .brand-suffix {
    display: block;
    font-weight: 400;
    font-size: 9px;
    text-align: right;
    margin-top: 3px;
    color: var(--ice);
  }
</style>
</head>
<body>

  <section class="card card-back" aria-label="Card back">
    <div class="brand">
      <div class="brand-square"></div>
      <div class="brand-name">Korvane<br>Motors</div>
    </div>
    <p class="website">www.korvane-motors.com.au</p>
  </section>

  <section class="card card-front" aria-label="Card front">
    <svg class="bolt" viewBox="0 0 540 310" preserveAspectRatio="none" aria-hidden="true">
      <polygon points="365,0 540,0 540,310 205,310 290,150 240,150" fill="var(--blue-main)"/>
      <polygon points="430,0 540,0 540,150 470,150 520,60 450,60" fill="#4a88c2" opacity="0.55"/>
      <polygon points="290,150 360,150 300,310 205,310" fill="var(--blue-deep)" opacity="0.18"/>
    </svg>

    <div class="contact">
      <h1 class="person">Marla Quenby</h1>
      <p class="address">14 Tallow Street, Carrow QLD 4178<br>PO Box 582, Wendell<br>QLD 4175</p>
      <ul class="lines">
        <li><svg viewBox="0 0 14 14"><path d="M2 5c0-2 2-3 5-3s5 1 5 3l-2 1-1-2H5L4 6z"/><rect x="3" y="7" width="8" height="5" rx="1"/></svg>+61 7 3555 0142</li>
        <li><svg viewBox="0 0 14 14"><rect x="4" y="1" width="6" height="12" rx="1"/><line x1="6" y1="11" x2="8" y2="11"/></svg>+61 400 555 218</li>
        <li><svg viewBox="0 0 14 14"><rect x="4" y="1" width="6" height="4"/><rect x="1.5" y="5" width="11" height="5" rx="1"/><rect x="4" y="9" width="6" height="4"/></svg>+61 7 3555 0199</li>
        <li><svg viewBox="0 0 14 14"><rect x="1" y="3" width="12" height="8"/><polyline points="1,3 7,8 13,3"/></svg>marla@korvane-motors.com.au</li>
      </ul>
    </div>

    <div class="brand">
      <div class="brand-square" style="background: var(--white); opacity: 0.9;"></div>
      <div class="brand-name">Korvane<br>Motors<span class="brand-suffix">Pty Ltd</span></div>
    </div>
  </section>

</body>
</html>
```